PPT Design Project for an educational startup

We seek a PPT design for a new company based in Japan called "Brivorent".
We provide PPT slide-based educational videos for free.
Please see the link below. You will see some videos.
http://velmora-example.jp/
The current template is also attached.
As we are changing our service name from Velmora to Brivorent, we are considering to change the PPT template as well.
Here are some notes regarding this project.
1. We need three pages;
- Title page: Letters for the tile and the logo are necessary. Some pictorial marks or other design would be appreciated.
- Contents page: Just one line to divide the message part and contents part should be sufficient. Please do not spend your time here.
- Final page: The word "Thank you for watching!" in the center. Some pictorial marks or other design would be appreciated.
2. Please use light green, orange, and purple as main colors. (Same as the current template)
3. You don't have to think about the font-style. This is going to be Japanese font, so we will take care of this.
4. Background color needs to be white, as the slides could be printed out.
5. We use Powerpoint for Mac.
6. No copyright section required, as these slides will be creative commons. Instead of the copyright section, please put the creative commons mark in all slides. (which is in the original template attached)
Updates
Please forget about the creative commons mark.
Hi all,
Target Market(s)
16-25 years old people, who are highly educated or highly motivated for education
Industry/Entity Type
It Company
Requirements
Must have
- 1. Creative commons mark (which is in the original template)
Should not have
- 1. Copyright mark

```html
<!DOCTYPE html>
<html lang="en">
<head>
<meta charset="utf-8">
<title>Brivorent Slide Template</title>
<link href="https://fonts.googleapis.com/css2?family=PT+Sans:wght@400;700&family=Arvo:wght@700&display=swap" rel="stylesheet">
<style>
  :root {
    --stage: #ececec;
    --slide: #ffffff;
    --ink: #555555;
    --heading: #7a7a7a;
    --rule: #c9c9c9;
    --green: #7cbb35;
    --orange: #e69a1e;
    --title-orange: #dd8a23;
    --red: #e2372a;
    --tab-green: #8cbf3a;
    --tab-yellow: #f2a51b;
    --purple: #8a4fa8;
  }
  * { box-sizing: border-box; margin: 0; padding: 0; }
  html, body { width: 1200px; height: 647px; overflow: hidden; }
  body {
    background: var(--stage);
    font-family: "PT Sans", Arial, sans-serif;
    color: var(--ink);
    position: relative;
  }
  .slide {
    position: absolute;
    width: 306px;
    height: 229px;
    background:
      radial-gradient(ellipse at 15% 20%, rgba(124,187,53,0.08), transparent 55%),
      radial-gradient(ellipse at 90% 85%, rgba(230,154,30,0.06), transparent 50%),
      var(--slide);
    box-shadow: 0 2px 6px rgba(0,0,0,0.18);
    overflow: hidden;
  }
  .slide--title   { left: 88px;  top: 68px; }
  .slide--steps   { left: 438px; top: 66px; }
  .slide--team    { left: 784px; top: 66px; }
  .slide--learn   { left: 252px; top: 355px; }
  .slide--closing { left: 607px; top: 355px; }

  .slide__url {
    position: absolute;
    left: 0; right: 0; bottom: 4px;
    text-align: center;
    font-size: 5.5px;
    font-weight: 700;
    color: var(--orange);
    letter-spacing: 0.2px;
  }
  .slide__heading {
    position: absolute;
    left: 13px; top: 7px;
    font-size: 13px;
    font-weight: 700;
    color: var(--heading);
    padding-bottom: 2px;
    border-bottom: 1px solid var(--rule);
    width: 80px;
  }
  .body-text {
    position: absolute;
    font-size: 5.7px;
    line-height: 8.2px;
    color: var(--ink);
    text-align: justify;
  }

  .wordmark {
    position: absolute;
    display: flex;
    align-items: center;
    gap: 5px;
    font-size: 34px;
    font-weight: 700;
    color: var(--heading);
    letter-spacing: -0.5px;
  }
  .wordmark__square {
    width: 9px; height: 9px;
    background: var(--orange);
  }

  .presentation-title {
    position: absolute;
    left: 0; width: 306px; top: 136px;
    text-align: center;
    font-size: 17px;
    color: var(--title-orange);
  }

  .step-tabs { position: absolute; left: 166px; top: 28px; width: 140px; }
  .step-tab {
    position: absolute;
    left: 0; width: 140px; height: 38px;
  }
  .step-tab svg { position: absolute; inset: 0; }
  .step-tab__num {
    position: absolute;
    left: 20px; top: 7px;
    font-size: 21px;
    font-weight: 700;
    color: #fff;
  }
  .step-tab__text {
    position: absolute;
    left: 53px; top: 9px; width: 52px;
    font-size: 4.6px;
    line-height: 5.8px;
    font-weight: 700;
    color: #fff;
  }

  .artwork { position: absolute; border-radius: 6px; }
  .artwork--team {
    left: 30px; top: 140px; width: 250px; height: 70px;
    background: linear-gradient(90deg, #d8453a, #f0a02a, #e9d13a, #7cbb35, #3f8ed6, #5a56b8, #8a4fa8, #c24a8a);
    opacity: 0.8;
  }
  .artwork--circle {
    left: 145px; top: 140px; width: 155px; height: 60px;
    border-radius: 50%;
    background: radial-gradient(ellipse at center, #ffffff 30%, #7cbb35 55%, #3f8ed6 70%, #8a4fa8 85%, #e2372a 100%);
    opacity: 0.75;
  }

  .point-list {
    position: absolute;
    left: 22px; top: 141px;
    list-style: none;
    font-size: 6px;
    font-weight: 700;
    color: var(--ink);
  }
  .point-list li {
    display: flex; align-items: center; gap: 5px;
    height: 13px;
  }
  .point-list li::before {
    content: "";
    width: 5px; height: 5px;
    border-radius: 50%;
    background: #777;
  }

  .thanks {
    position: absolute;
    left: 0; width: 306px; top: 145px;
    text-align: center;
  }
  .thanks__main {
    font-family: "Arvo", Georgia, serif;
    font-size: 22px;
    color: var(--green);
  }
  .thanks__sub {
    font-size: 12px;
    font-weight: 700;
    color: var(--orange);
    margin-top: 1px;
  }
</style>
</head>
<body>

  <section class="slide slide--title">
    <div class="wordmark" style="left:60px; top:40px;">Brivorent<span class="wordmark__square"></span></div>
    <p class="presentation-title">Presentation Title</p>
    <p class="slide__url">www.brivorent.jp</p>
  </section>

  <section class="slide slide--steps">
    <h2 class="slide__heading">Lorem Ipsum</h2>
    <p class="body-text" style="left:13px; top:32px; width:152px;">Lorem ipsum dolor sit amet, consectetuer adipiscing elit, sed diam nonummy nibh euismod tincidunt ut laoreet dolore magna aliquam erat volutpat. Ut wisi enim ad minim veniam, quis nostrud exerci tation ullamcoper suscipit lobortis.</p>
    <p class="body-text" style="left:13px; top:91px; width:152px;">Lorem ipsum dolor sit amet, consectetuer adipiscing elit, sed diam nonummy nibh euismod tincidunt ut laoreet dolore magna aliquam erat volutpat. Ut wisi enim ad minim veniam, quis nostrud exerci tation ullamcoper suscipit lobortis.</p>
    <p class="body-text" style="left:13px; top:154px; width:152px;">Lorem ipsum dolor sit amet, consectetuer adipiscing elit, sed diam nonummy nibh euismod tincidunt ut laoreet dolore magna aliquam erat volutpat. Ut wisi enim ad minim veniam, quis nostrud exerci tation ullamcoper suscipit lobortis.</p>

    <div class="step-tabs">
      <div class="step-tab" style="top:0;">
        <svg width="140" height="38" viewBox="0 0 140 38"><path d="M14 3 H140 V35 H14 L2 19 Z" fill="var(--red)"/><path d="M44 7 V31" stroke="#fff" stroke-width="0.6" opacity="0.7"/></svg>
        <span class="step-tab__num">01</span>
        <span class="step-tab__text">Plan your study goal each week</span>
      </div>
      <div class="step-tab" style="top:62px;">
        <svg width="140" height="38" viewBox="0 0 140 38"><path d="M14 3 H140 V35 H14 L2 19 Z" fill="var(--tab-yellow)"/><path d="M44 7 V31" stroke="#fff" stroke-width="0.6" opacity="0.7"/></svg>
        <span class="step-tab__num">02</span>
        <span class="step-tab__text">Review notes after every lesson</span>
      </div>
      <div class="step-tab" style="top:124px;">
        <svg width="140" height="38" viewBox="0 0 140 38"><path d="M14 3 H140 V35 H14 L2 19 Z" fill="var(--tab-green)"/><path d="M44 7 V31" stroke="#fff" stroke-width="0.6" opacity="0.7"/></svg>
        <span class="step-tab__num">03</span>
        <span class="step-tab__text">Practice with short quizzes daily</span>
      </div>
    </div>
    <p class="slide__url">www.brivorent.jp</p>
  </section>

  <section class="slide slide--team">
    <h2 class="slide__heading">Lorem Ipsum</h2>
    <p class="body-text" style="left:20px; top:34px; width:266px;">Lorem ipsum dolor sit amet, consectetuer adipiscing elit, sed diam nonummy nibh euismod tincidunt ut laoreet dolore magna aliquam erat volutpat. Ut wisi enim ad minim veniam, quis nostrud exerci tation ullamcorper suscipit lobortis nisl ut aliquip ex ea commodo consequat. Duis autem vel eum iriure dolor in hendrerit in vulputate velit esse molestie consequat, vel illum dolore eu feugiat nulla facilisis.</p>
    <p class="body-text" style="left:20px; top:84px; width:266px;">Lorem ipsum dolor sit amet, consectetuer adipiscing elit, sed diam nonummy nibh euismod tincidunt ut laoreet dolore magna aliquam erat volutpat. Ut wisi enim ad minim veniam, quis nostrud exerci tation ullamcorper suscipit lobortis nisl ut aliquip ex ea commodo consequat. Duis autem vel eum iriure dolor in hendrerit in vulputate velit esse molestie consequat, vel illum dolore eu feugiat nulla facilisis.</p>
    <div class="artwork artwork--team" role="img" aria-label="Row of colourful clay figures linked arm in arm"></div>
    <p class="slide__url">www.brivorent.jp</p>
  </section>

  <section class="slide slide--learn">
    <h2 class="slide__heading" style="left:22px;">Lorem Ipsum</h2>
    <p class="body-text" style="left:22px; top:34px; width:266px;">Lorem ipsum d olor sit amet, consectetuer adipiscing elit, sed diam nonummy nibh euismod tincidunt ut laoreet dolore magna aliquam erat volutpat. Ut wisi enim ad minim veniam, quis nostrud exerci tation ullamcorper suscipit lobortis nisl ut aliquip ex ea commodo consequat. Duis autem vel eum iriure dolor in hendrerit in vulputate velit esse molestie consequat, vel illum dolore eu feugiat nulla facilisis.</p>
    <p class="body-text" style="left:22px; top:84px; width:266px;">Lorem ipsum d olor sit amet, consectetuer adipiscing elit, sed diam nonummy nibh euismod tincidunt ut laoreet dolore magna aliquam erat volutpat. Ut wisi enim ad minim veniam, quis nostrud exerci tation ullamcorper suscipit lobortis nisl ut aliquip ex ea commodo consequat. Duis autem vel eum iriure dolor in hendrerit in vulputate velit esse molestie consequat, vel illum dolore eu feugiat nulla facilisis.</p>
    <ul class="point-list">
      <li>Lorem ipsum Lorem Lorem ipsum</li>
      <li>Lorem ipsum Lorem Lorem</li>
      <li>Lorem ipsum Lorem Lorem ipsum</li>
      <li>Lorem ipsum orem Lorem ipsum</li>
    </ul>
    <div class="artwork artwork--circle" role="img" aria-label="Ring of colourful figures around the word Learn"></div>
    <p class="slide__url">www.brivorent.jp</p>
  </section>

  <section class="slide slide--closing">
    <div class="wordmark" style="left:60px; top:34px;">Brivorent<span class="wordmark__square"></span></div>
    <div class="thanks">
      <p class="thanks__main">Thank You!</p>
      <p class="thanks__sub">for watching!</p>
    </div>
    <p class="slide__url">www.brivorent.jp</p>
  </section>

</body>
</html>
```